Oil and Gas Exploration and Production company needs a business card design

We need a business card design using our logo and colors in the logo. We want a mainstream design.

```html
<!DOCTYPE html>
<html lang="en">
<head>
<meta charset="utf-8">
<title>Corvan Oil &amp; Gas — Business Card</title>
<link rel="stylesheet" href="https://fonts.googleapis.com/css2?family=Lato:wght@400;700;900&display=swap">
<style>
  :root {
    --page-bg: #f1f1f1;
    --card-bg: #ffffff;
    --ink: #111111;
    --text-grey: #555555;
    --gold: #c8952a;
    --rule: #d6d6d6;
  }
  * { margin: 0; padding: 0; box-sizing: border-box; }
  html, body {
    width: 1200px;
    height: 1200px;
    overflow: hidden;
    background: var(--page-bg);
    font-family: "Lato", sans-serif;
  }
  .business-card {
    position: absolute;
    left: 246px;
    top: 406px;
    width: 706px;
    height: 402px;
    background: var(--card-bg);
    border-radius: 24px;
  }
  .brand {
    position: absolute;
    left: 89px;
    top: 158px;
    display: flex;
    align-items: center;
    gap: 12px;
  }
  .brand-dot {
    width: 40px;
    height: 40px;
    border-radius: 50%;
    background: var(--gold);
    flex: none;
  }
  .brand-name {
    font-weight: 900;
    color: var(--ink);
    font-size: 38px;
    line-height: 1;
    letter-spacing: -0.5px;
  }
  .brand-name span { display: block; font-size: 22px; letter-spacing: 4px; margin-top: 6px; }
  .divider {
    position: absolute;
    left: 354px;
    top: 97px;
    width: 2px;
    height: 205px;
    background: var(--rule);
  }
  .contact { position: absolute; left: 377px; top: 0; }
  .person-name {
    position: absolute;
    top: 94px;
    white-space: nowrap;
    font-size: 29px;
    font-weight: 700;
    color: var(--ink);
    line-height: 1;
  }
  .person-role {
    position: absolute;
    top: 131px;
    font-size: 17px;
    font-weight: 700;
    color: var(--gold);
    line-height: 1;
  }
  .address {
    position: absolute;
    top: 170px;
    left: 2px;
    white-space: nowrap;
    font-size: 17px;
    color: var(--text-grey);
    line-height: 24px;
  }
  .contact-list {
    position: absolute;
    top: 233px;
    left: 2px;
    list-style: none;
  }
  .contact-list li {
    display: flex;
    align-items: center;
    height: 24.5px;
    white-space: nowrap;
    font-size: 17px;
    color: var(--text-grey);
  }
  .contact-list svg { width: 12px; height: 12px; margin-right: 15px; fill: var(--gold); flex: none; }
  .accent { color: var(--gold); }
</style>
</head>
<body>
  <div class="business-card">
    <div class="brand">
      <div class="brand-dot"></div>
      <div class="brand-name">Corvan<span>OIL &amp; GAS</span></div>
    </div>

    <div class="divider"></div>

    <div class="contact">
      <div class="person-name">Daniel Hart</div>
      <div class="person-role">President</div>
      <div class="address">Unit 4/210 Kestrel Rd<br>Port Avalon SA 5700</div>
      <ul class="contact-list">
        <li>
          <svg viewBox="0 0 24 24" aria-hidden="true"><path d="M6.6 10.8a15.1 15.1 0 0 0 6.6 6.6l2.2-2.2c.3-.3.7-.4 1-.2 1.1.4 2.3.6 3.6.6.6 0 1 .4 1 1V20c0 .6-.4 1-1 1A17 17 0 0 1 3 4c0-.6.4-1 1-1h3.5c.6 0 1 .4 1 1 0 1.3.2 2.5.6 3.6.1.3 0 .7-.2 1z"/></svg>
          (08) 5550 1824
        </li>
        <li>
          <svg viewBox="0 0 24 24" aria-hidden="true"><path d="M2 5h20v2l-10 6L2 7z"/><path d="M2 9.3l10 6 10-6V19H2z"/></svg>
          info@yourmail.com
        </li>
        <li>
          <svg viewBox="0 0 24 24" aria-hidden="true"><path d="M12 2a10 10 0 1 0 0 20 10 10 0 0 0 0-20zm6.9 6h-2.9a15 15 0 0 0-1.4-3.6A8 8 0 0 1 18.9 8zM12 4c.8 1.2 1.5 2.5 1.9 4h-3.8c.4-1.5 1.1-2.8 1.9-4zM4.3 14a8 8 0 0 1 0-4h3.4a16 16 0 0 0 0 4zm.8 2h2.9c.3 1.3.8 2.5 1.4 3.6A8 8 0 0 1 5.1 16zM8 8H5.1a8 8 0 0 1 4.3-3.6C8.8 5.5 8.3 6.7 8 8zm4 12c-.8-1.2-1.5-2.5-1.9-4h3.8c-.4 1.5-1.1 2.8-1.9 4zm2.3-6H9.7a14 14 0 0 1 0-4h4.6a14 14 0 0 1 0 4zm.3 5.6c.6-1.1 1.1-2.3 1.4-3.6h2.9a8 8 0 0 1-4.3 3.6zm1.7-5.6a16 16 0 0 0 0-4h3.4a8 8 0 0 1 0 4z"/></svg>
          www.<span class="accent">yourwebsite</span>.com
        </li>
      </ul>
    </div>
  </div>
</body>
</html>
```